Full Page Appliance Ad

Create a full page ad (7.5" W x 10" H) representing that we are a full service appliance company, where we have a showroom located at 14 N. Larkmoor Avenue Souderton, PA 18977. Our website is www.qbtrevolt.com , and our phone number is 215-846-3190. We don't only sell appliances, we deliver, install, and service. We also offer an additional year warranty* (see store for details). In addition to appliances, we also have an Electrical Department that specializes in residential applications.
May be best if split the full page ad into two spots. One spot to reference appliances, and the other to represent electrical.
I want it to look clean, and not too busy
30-70 years old

```html
<!DOCTYPE html>
<html lang="en">
<head>
<meta charset="UTF-8">
<title>Full Service Appliance Ad</title>
<link href="https://fonts.googleapis.com/css2?family=Poppins:wght@400;500;600;700;800&display=swap" rel="stylesheet">
<style>
  :root {
    --navy: #1c2340;
    --navy-deep: #141a33;
    --orange: #f7a823;
    --magenta: #d0245f;
    --magenta-light: #e8457a;
    --white: #ffffff;
    --ink: #1e1e24;
    --grey: #55585f;
  }
  * { box-sizing: border-box; margin: 0; padding: 0; }
  html, body { width: 900px; height: 1200px; overflow: hidden; background: var(--white); }
  body { font-family: "Poppins", sans-serif; color: var(--ink); }
  .ad { position: relative; width: 900px; height: 1200px; overflow: hidden; background: var(--white); }

  .hero {
    position: absolute; left: 0; top: 0; width: 900px; height: 695px;
    background: linear-gradient(180deg, #1a2140 0%, #232b52 55%, #2c3561 100%);
  }
  .hero-photo {
    position: absolute; left: 235px; top: 150px; width: 650px; height: 550px;
    background: radial-gradient(ellipse at 55% 45%, #d9dde3 0%, #a9afb9 45%, #5c6478 80%, rgba(44,53,97,0) 100%);
    border-radius: 18px;
  }

  .headline {
    position: absolute; left: 30px; top: 22px; width: 850px;
    color: var(--white); font-weight: 800; font-size: 51px; line-height: 1.22;
    letter-spacing: 0.5px; text-transform: uppercase;
  }
  .headline .accent { color: var(--orange); }
  .tagline {
    position: absolute; left: 30px; top: 168px;
    color: var(--white); font-weight: 600; font-size: 31px;
  }
  .tagline .accent { color: var(--orange); }

  .services { position: absolute; left: 30px; top: 230px; list-style: none; }
  .services li {
    display: flex; align-items: center; gap: 10px;
    color: var(--white); font-weight: 600; font-size: 23px; height: 35px;
  }
  .check-box { width: 24px; height: 24px; }

  .warranty { position: absolute; left: 40px; top: 462px; width: 150px; height: 255px; }
  .warranty-text {
    position: absolute; left: 40px; top: 508px; width: 130px;
    text-align: center; color: var(--white);
  }
  .warranty-num { font-size: 64px; font-weight: 800; line-height: 1; }
  .warranty-up { font-size: 12px; font-weight: 700; letter-spacing: 1px; margin-top: 4px; }
  .warranty-title { font-size: 17px; font-weight: 800; line-height: 1.2; margin-top: 2px; }
  .warranty-stars { color: var(--orange); font-size: 20px; letter-spacing: 8px; margin-top: 8px; }

  .catalog { position: absolute; left: 36px; top: 742px; width: 400px; height: 340px; }
  .category { position: absolute; display: flex; gap: 12px; }
  .category-icon {
    flex: none; width: 40px; height: 40px; border-radius: 4px;
    background: linear-gradient(160deg, #e4e6ea 0%, #9ea3ab 100%);
  }
  .category-icon.wide { width: 52px; height: 22px; margin-top: 4px; }
  .category-icon.round { border-radius: 50%; background: linear-gradient(160deg, #4a4d55 0%, #16181d 100%); }
  .category-list { list-style: none; font-size: 10px; line-height: 1.32; color: var(--ink); font-weight: 500; }
  .category-list .category-name { font-weight: 700; text-transform: uppercase; }

  .showroom {
    position: absolute; left: 36px; top: 1100px;
    display: flex; align-items: center; gap: 8px;
    font-size: 13px; font-weight: 600; color: var(--navy);
  }

  .electric-photo {
    position: absolute; left: 442px; top: 697px; width: 433px; height: 216px;
    background: linear-gradient(120deg, #2b3a55 0%, #5a6f8c 45%, #9aa6b4 75%, #d6d2c6 100%);
  }
  .electric-panel {
    position: absolute; left: 442px; top: 913px; width: 433px; height: 195px;
    background: var(--orange); padding: 16px 22px 0 22px;
  }
  .electric-title { font-size: 26px; font-weight: 800; color: var(--navy); letter-spacing: 0.3px; line-height: 1.3; }
  .electric-columns { display: flex; gap: 14px; margin-top: 8px; }
  .electric-list { list-style: none; font-size: 11px; font-weight: 600; color: var(--navy); line-height: 1.36; white-space: nowrap; }
  .electric-list li::before { content: "\2714"; margin-right: 3px; }

  .phone-tab {
    position: absolute; left: 633px; top: 1068px; width: 242px; height: 52px;
    background: var(--white); border-radius: 8px 0 0 8px;
    box-shadow: 0 3px 10px rgba(0,0,0,0.25);
    display: flex; align-items: center; padding-left: 14px;
    font-size: 22px; font-weight: 500; color: var(--ink);
  }
  .phone-tab .divider { width: 1px; height: 32px; background: #9a9a9a; margin: 0 14px 0 10px; }

  .footer {
    position: absolute; left: 0; top: 1138px; width: 900px; height: 62px;
    background: var(--navy); display: flex; align-items: center;
    color: var(--white); font-size: 27px; font-weight: 500;
  }
  .footer-item { display: flex; align-items: center; gap: 10px; }
  .footer-phone { margin-left: 36px; }
  .footer-web { margin-left: 70px; }
</style>
</head>
<body>
<main class="ad">
  <section class="hero">
    <div class="hero-photo" role="img" aria-label="Group of stainless steel appliances: refrigerators, range, dishwasher, washer, microwave, blender, coffee maker and toaster"></div>

    <h1 class="headline">Your <span class="accent">One Stop Shop</span> For<br>Electrical Appliances</h1>
    <p class="tagline">We’ll Take Care Of <span class="accent">Everything!</span></p>

    <ul class="services">
      <li>WE SELL <svg class="check-box" viewBox="0 0 24 24"><rect x="1" y="1" width="22" height="22" rx="3" fill="#fff"/><path d="M6 12.5l4 4 8-9" fill="none" stroke="#1c2340" stroke-width="3" stroke-linecap="round" stroke-linejoin="round"/></svg></li>
      <li>WE DELIVER <svg class="check-box" viewBox="0 0 24 24"><rect x="1" y="1" width="22" height="22" rx="3" fill="#fff"/><path d="M6 12.5l4 4 8-9" fill="none" stroke="#1c2340" stroke-width="3" stroke-linecap="round" stroke-linejoin="round"/></svg></li>
      <li>WE INSTALL <svg class="check-box" viewBox="0 0 24 24"><rect x="1" y="1" width="22" height="22" rx="3" fill="#fff"/><path d="M6 12.5l4 4 8-9" fill="none" stroke="#1c2340" stroke-width="3" stroke-linecap="round" stroke-linejoin="round"/></svg></li>
      <li>WE SERVICE <svg class="check-box" viewBox="0 0 24 24"><rect x="1" y="1" width="22" height="22" rx="3" fill="#fff"/><path d="M6 12.5l4 4 8-9" fill="none" stroke="#1c2340" stroke-width="3" stroke-linecap="round" stroke-linejoin="round"/></svg></li>
    </ul>
  </section>

  <svg class="warranty" viewBox="0 0 150 255" aria-hidden="true">
    <defs>
      <linearGradient id="ribbonFill" x1="0" y1="0" x2="0" y2="1">
        <stop offset="0" stop-color="#b81d55"/>
        <stop offset="1" stop-color="#e8457a"/>
      </linearGradient>
    </defs>
    <path d="M2 45 L130 20 L130 255 L66 222 L2 255 Z" fill="url(#ribbonFill)"/>
    <path d="M0 30 Q0 14 18 12 L148 0 L148 22 L18 36 Q6 38 2 48 Z" fill="#f7a823"/>
    <path d="M0 30 Q0 46 14 44 L18 36 Q6 38 2 48" fill="#c97f0c"/>
  </svg>
  <div class="warranty-text">
    <div class="warranty-num">1</div>
    <div class="warranty-up">UP TO</div>
    <div class="warranty-title">ONE YEAR<br>WARRANTY</div>
    <div class="warranty-stars">★★★</div>
  </div>

  <section class="catalog">
    <div class="category" style="left:0; top:0;">
      <div class="category-icon" role="img" aria-label="Range"></div>
      <ul class="category-list"><li class="category-name">Cooking</li><li>Ranges &amp; Cooktops</li><li>Wall Ovens</li><li>Range Hoods</li><li>Microwaves</li></ul>
    </div>
    <div class="category" style="left:0; top:82px;">
      <div class="category-icon" role="img" aria-label="Refrigerator"></div>
      <ul class="category-list"><li class="category-name">Refridgeration</li><li>Refridgerators</li><li>Freezers</li><li>Ice Makers</li><li>Beverage Centers</li><li>Refridgerated Drawers</li></ul>
    </div>
    <div class="category" style="left:0; top:184px;">
      <div class="category-icon" role="img" aria-label="Washer and dryer"></div>
      <ul class="category-list"><li class="category-name">Laundry</li><li>Washers</li><li>Dryers</li><li>Hoses &amp; Accessories</li><li>Laundry Pedestals</li></ul>
    </div>
    <div class="category" style="left:0; top:272px;">
      <div class="category-icon" role="img" aria-label="Dishwasher"></div>
      <ul class="category-list"><li class="category-name">Dishwashers</li><li>Built-In Dishwashers</li><li>Portable Dishwashers</li><li>Trash Compactors</li><li>Waste Disposals</li></ul>
    </div>
    <div class="category" style="left:196px; top:0;">
      <div class="category-icon round" role="img" aria-label="Kettle grill"></div>
      <ul class="category-list"><li class="category-name">Outdoor</li><li>Gas Grills</li><li>Charcoal Grills</li><li>Electric Grills</li><li>Pellet Grills</li><li>Pro-style Grills</li><li>Grill Accessories</li></ul>
    </div>
    <div class="category" style="left:196px; top:108px;">
      <div class="category-icon" role="img" aria-label="Water heater"></div>
      <ul class="category-list"><li class="category-name">Water Treatment</li><li>Electric Water Heaters</li><li>Gas Water Heaters</li><li>Water Softeners</li><li>Water Filters</li></ul>
    </div>
    <div class="category" style="left:196px; top:185px;">
      <div class="category-icon wide" role="img" aria-label="Wall air conditioner"></div>
      <ul class="category-list"><li class="category-name">Air Control</li><li>Air Conditioners</li><li>A/C Accessories</li><li>Heaters</li><li>Humidifiers</li><li>Dehumidifiers</li></ul>
    </div>
  </section>

  <p class="showroom">
    <svg width="14" height="18" viewBox="0 0 14 18" aria-hidden="true"><path d="M7 0a7 7 0 00-7 7c0 5 7 11 7 11s7-6 7-11a7 7 0 00-7-7z" fill="#1c2340"/><circle cx="7" cy="7" r="2.6" fill="#fff"/></svg>
    <span>Showroom: 14 N. Larkmoor Avenue Souderton, PA 18977</span>
  </p>

  <div class="electric-photo" role="img" aria-label="Electrician in hard hat and safety glasses working on an electrical panel"></div>
  <section class="electric-panel">
    <h2 class="electric-title">NEED AN ELECTRICIAN?</h2>
    <div class="electric-columns">
      <ul class="electric-list"><li>Troubleshooting</li><li>Service Upgrades</li><li>Remodel Wiring</li><li>Wire Trenching</li><li>Landscape Lighting</li></ul>
      <ul class="electric-list"><li>Under Cabinet Lighting</li><li>Surge Protection</li><li>Ceiling Fan Installation, Replacement</li><li>Generator Installation &amp; Hookup</li><li>Data &amp; Communication Wiring</li></ul>
    </div>
  </section>

  <div class="phone-tab">
    <svg width="24" height="24" viewBox="0 0 24 24" aria-hidden="true"><path d="M6.6 10.8a15.1 15.1 0 006.6 6.6l2.2-2.2a1 1 0 011-.25 11.4 11.4 0 003.6.57 1 1 0 011 1V20a1 1 0 01-1 1A17 17 0 013 4a1 1 0 011-1h3.5a1 1 0 011 1c0 1.250.2 2.450.57 3.6a1 1 0 01-.25 1z" fill="#555"/></svg>
    <span class="divider"></span>
    <span>215-846-3190</span>
  </div>

  <footer class="footer">
    <div class="footer-item footer-phone">
      <svg width="28" height="28" viewBox="0 0 24 24" aria-hidden="true"><rect x="3" y="9" width="18" height="12" rx="2" fill="none" stroke="#fff" stroke-width="1.6"/><path d="M5 9 Q12 2 19 9" fill="none" stroke="#fff" stroke-width="1.6"/><circle cx="12" cy="15" r="3" fill="none" stroke="#fff" stroke-width="1.4"/></svg>
      <span>215-846-3190</span>
    </div>
    <div class="footer-item footer-web">
      <svg width="28" height="28" viewBox="0 0 24 24" aria-hidden="true"><g fill="none" stroke="#fff" stroke-width="1.6"><circle cx="12" cy="12" r="9.5"/><ellipse cx="12" cy="12" rx="4.2" ry="9.5"/><path d="M2.5 12h19M4 7h16M4 17h16"/></g></svg>
      <span>www.qbtrevoltappliances.com</span>
    </div>
  </footer>
</main>
</body>
</html>
```